Women's Health Company needs business card

We need a business card for a USA based women's health care company. We use digital technology to enhance therapy prescribed by clinicians for their patients

```html
<!DOCTYPE html>
<html lang="en">
<head>
<meta charset="utf-8">
<title>Lumira Health – Business Card</title>
<link href="https://fonts.googleapis.com/css2?family=Montserrat:wght@300;400;500&display=swap" rel="stylesheet">
<style>
  :root {
    --bg: #2a2a30;
    --card-white: #ffffff;
    --card-tint: #f1f1f2;
    --teal: #5fbcb8;
    --purple: #9152a3;
    --purple-deep: #7f4391;
    --grey-text: #8a8a8f;
    --body-text: #6e6e73;
  }
  * { margin: 0; padding: 0; box-sizing: border-box; }
  html, body { width: 1200px; height: 817px; overflow: hidden; }
  body {
    background: var(--bg);
    font-family: "Montserrat", sans-serif;
    display: flex;
    align-items: center;
    justify-content: center;
    gap: 40px;
  }
  .card {
    width: 540px;
    height: 310px;
    border-radius: 34px;
    position: relative;
    overflow: hidden;
  }
  .card--front {
    background: radial-gradient(circle at 45% 55%, var(--card-white) 0%, var(--card-tint) 100%);
  }
  .card--back {
    background: var(--purple);
    display: flex;
    align-items: center;
    justify-content: center;
  }
  .brand {
    position: absolute;
    left: 44px;
    top: 96px;
    display: flex;
    align-items: center;
    gap: 10px;
    color: var(--teal);
    font-weight: 400;
    font-size: 34px;
    letter-spacing: 0.5px;
  }
  .brand__dot {
    width: 10px; height: 10px; border-radius: 50%;
    background: var(--teal);
  }
  .holder {
    position: absolute;
    right: 40px;
    top: 34px;
    text-align: right;
  }
  .holder__name {
    font-size: 24px;
    font-weight: 400;
    letter-spacing: 1px;
    text-transform: uppercase;
    color: var(--teal);
  }
  .holder__name .surname { color: var(--purple); }
  .holder__title {
    font-size: 15px;
    font-weight: 400;
    color: var(--grey-text);
    margin-top: 2px;
  }
  .contact {
    position: absolute;
    left: 44px;
    bottom: 30px;
    font-size: 13px;
    line-height: 1.5;
    color: var(--body-text);
    list-style: none;
  }
  .contact__address { margin-bottom: 8px; }
  .contact__item { display: flex; align-items: center; gap: 8px; }
  .contact__item svg { width: 12px; height: 12px; fill: var(--purple); flex: none; }
  .back-brand {
    color: var(--purple-deep);
    font-weight: 400;
    font-size: 46px;
    letter-spacing: 1px;
  }
</style>
</head>
<body>
  <section class="card card--front" aria-label="Business card front">
    <div class="brand"><span class="brand__dot"></span>Lumira Health</div>

    <div class="holder">
      <p class="holder__name">Mara <span class="surname">Ellis</span></p>
      <p class="holder__title">Manager</p>
    </div>

    <ul class="contact">
      <li class="contact__address">214 Willow Creek Road<br>Boulder Colorado 80301</li>
      <li class="contact__item">
        <svg viewBox="0 0 24 24"><path d="M6.6 10.8a15.1 15.1 0 0 0 6.6 6.6l2.2-2.2a1 1 0 0 1 1-.25 11.4 11.4 0 0 0 3.6.57 1 1 0 0 1 1 1V20a1 1 0 0 1-1 1A17 17 0 0 1 3 4a1 1 0 0 1 1-1h3.5a1 1 0 0 1 1 1c0 1.25.2 2.45.57 3.57a1 1 0 0 1-.25 1z"/></svg>
        555-318-2046
      </li>
      <li class="contact__item">
        <svg viewBox="0 0 24 24"><path d="M2 5h20v14H2zm2 2v.5l8 5 8-5V7z"/></svg>
        hello@lumirahealth.com
      </li>
      <li class="contact__item">
        <svg viewBox="0 0 24 24"><path d="M12 2a10 10 0 1 0 0 20 10 10 0 0 0 0-20zm6.9 9h-3a15 15 0 0 0-1.3-5.6A8 8 0 0 1 18.9 11zM12 4.1c.9 1.3 1.8 3.6 1.9 6.9h-3.8c.1-3.3 1-5.6 1.9-6.9zM9.4 5.4A15 15 0 0 0 8.1 11h-3a8 8 0 0 1 4.3-5.6zM5.1 13h3a15 15 0 0 0 1.3 5.6A8 8 0 0 1 5.1 13zm6.9 6.9c-.9-1.3-1.8-3.6-1.9-6.9h3.8c-.1 3.3-1 5.6-1.9 6.9zm2.6-1.3a15 15 0 0 0 1.3-5.6h3a8 8 0 0 1-4.3 5.6z"/></svg>
        www.lumirahealth.com
      </li>
    </ul>
  </section>

  <section class="card card--back" aria-label="Business card back">
    <p class="back-brand">Lumira Health</p>
  </section>
</body>
</html>
```